Creation of foldable A4 Leaflet to summarise my website

I need to summarize the content of my website into a 4 facecs-2 pages A4 foldable leaflet. I need the leaflet to go through the main topics of my website, with accurate descriptions and some pics taken from the website. Focusing about professionality and over 25 year experience on the field. Give also apace to our valued partners and customers
My website plimborex.au

Target Market(s)

Industrial filtration, dust collector business

Industry/Entity Type

Industrial filtration, dust collectors market, mining, powerplant, cement industry

Font styles to use
Sans Serif

Colors
0054AA
0677BA
7BADD7
CADEEF
E8F1F8

Requirements
Must have
• clear references to my website
Nice to have
• clear and clean layout
Should not have
• dark colours other than blue and navy, as per my logo

```html
<!DOCTYPE html>
<html lang="en">
<head>
<meta charset="utf-8">
<title>Plimborex Environmental Services – Leaflet</title>
<link href="https://fonts.googleapis.com/css2?family=Montserrat:wght@400;500;600;700;800&display=swap" rel="stylesheet">
<style>
:root{
  --navy:#1b2d58;
  --blue:#0054aa;
  --mid:#0677ba;
  --sky:#7badd7;
  --pale:#cadeef;
  --ice:#e8f1f8;
  --ink:#1f2a3c;
  --stage:#dcdde0;
}
*{margin:0;padding:0;box-sizing:border-box}
html,body{width:1200px;height:1024px;overflow:hidden;background:var(--stage);font-family:"Montserrat",sans-serif;color:var(--ink)}
.spread{position:absolute;left:260px;width:680px;height:481px;display:flex;box-shadow:0 6px 18px rgba(0,0,0,.18)}
.spread.outside{top:18px}
.spread.inside{top:523px}
.page{position:relative;width:340px;height:481px;overflow:hidden;background:linear-gradient(180deg,#fff 0%,var(--ice) 100%)}
.abs{position:absolute}

/* back cover */
.back-photo{position:absolute;inset:0;background:radial-gradient(ellipse at 30% 30%,#4f8fd9 0%,#1f64c4 45%,#0f4fae 100%)}
.contact{position:absolute;left:0;right:0;top:300px;text-align:center;color:#fff}
.contact .kicker{font-size:8px;font-weight:500;letter-spacing:.5px}
.contact h3{font-size:15px;font-weight:800;color:var(--navy);margin-top:3px}
.contact .lead{font-size:6.5px;font-weight:500;line-height:1.4;margin:4px auto 0;width:200px}
.contact .phone{font-size:15px;font-weight:800;margin-top:14px;display:flex;align-items:center;justify-content:center;gap:5px}
.contact .line{font-size:9px;font-weight:600;margin-top:8px;display:flex;align-items:center;justify-content:center;gap:5px}
.contact svg{flex:none}

/* front cover */
.cover-art{position:absolute;left:0;top:0}
.brand{position:absolute;display:flex;align-items:center;gap:8px}
.brand .mark{width:40px;height:40px;border:5px solid var(--navy);background:var(--sky)}
.brand .name{font-size:22px;font-weight:800;color:var(--navy);letter-spacing:.5px;line-height:1}
.brand .sub{font-size:7.5px;font-weight:700;color:var(--blue);letter-spacing:2.6px;line-height:1.5;margin-top:3px;text-align:center}
.cover-label{font-size:6px;color:var(--blue);font-weight:500}
.cover-title{font-size:15px;font-weight:800;color:var(--navy);line-height:1.18}
.cover-rule{height:1px;background:var(--sky)}
.cover-blurb{font-size:7.2px;color:var(--blue);line-height:1.5;font-weight:500}
.url-tag{background:var(--blue);color:#fff;font-size:6.5px;font-weight:700;padding:2px 8px 2px 26px;letter-spacing:.3px}
.hex-ghost{position:absolute;opacity:.35}

/* inside pages */
.h-section{font-size:15px;font-weight:800;color:var(--navy);border-left:2px solid var(--blue);padding-left:5px;line-height:1}
.h-sub{font-size:8.5px;font-weight:700;color:var(--blue);line-height:1.25}
.body{font-size:5.4px;line-height:1.42;color:var(--ink)}
.body p+p{margin-top:6px}
.photo-oct{position:absolute}
.services-panel{position:absolute;left:0;top:300px;width:128px;height:181px;background:linear-gradient(180deg,#2f72c4,#5b94d4);border-top-right-radius:14px;padding:11px 10px 0 14px;color:#fff}
.services-panel h4{font-size:10.5px;font-weight:800;margin-bottom:5px}
.services-panel li{font-size:5.4px;line-height:1.3;list-style:none;position:relative;padding-left:6px;margin-bottom:3.6px}
.services-panel li::before{content:"";position:absolute;left:0;top:2px;width:2px;height:2px;border-radius:50%;background:#fff}
.svc{position:absolute;width:80px}
.svc h5{font-size:5.8px;font-weight:700;color:var(--blue);border-left:1.5px solid var(--blue);padding-left:4px;line-height:1.25;margin-bottom:8px}
.svc p{font-size:4.9px;line-height:1.4;padding-left:5px}

.why{position:absolute;left:0;top:300px;width:340px;height:170px;background:linear-gradient(120deg,#22375f 0%,#1b2d58 60%,#24406e 100%)}
.why-copy{position:absolute;left:12px;top:16px;color:#fff;width:140px}
.why-copy .k{font-size:9px;font-weight:500}
.why-copy .big{font-size:17px;font-weight:800;color:var(--sky);line-height:1}
.why-copy .big span{font-size:9px;color:#fff;font-weight:500}
.why-copy p{font-size:6.5px;font-weight:600;line-height:1.35;margin-top:10px}
.clients{position:absolute;left:158px;top:360px;width:170px;height:121px;background:#f3f6fa;border-radius:8px 8px 0 0;padding:10px 8px}
.clients h4{text-align:center;font-size:11px;font-weight:800;color:var(--navy);margin-bottom:8px}
.client-grid{display:grid;grid-template-columns:repeat(4,1fr);gap:6px 4px}
.client{display:flex;align-items:center;gap:2px;font-size:4.6px;font-weight:700;color:var(--navy);white-space:nowrap}
.client i{width:4px;height:4px;background:var(--blue);flex:none}
</style>
</head>
<body>

<section class="spread outside">
  <div class="page back-cover">
    <div class="back-photo" role="img" aria-label="Soft-focus blue close-up of filter bag fabric"></div>
    <div class="contact">
      <div class="kicker">CONTACT US</div>
      <h3>GET IN TOUCH</h3>
      <p class="lead">Fill in your details below and we'll get back to you as soon as possible or call us directly:</p>
      <div class="phone">
        <svg width="9" height="12" viewBox="0 0 9 12"><path d="M3 1 C0 3 0 9 3 11 L4.5 9 C3 8 3 4 4.5 3 Z" fill="#fff"/></svg>
        0412 555 019
      </div>
      <div class="line">
        <svg width="9" height="7" viewBox="0 0 9 7"><rect x=".5" y=".5" width="8" height="6" fill="none" stroke="#fff"/><path d="M.5 .5 4.5 4 8.5 .5" fill="none" stroke="#fff"/></svg>
        hello@plimborex.au
      </div>
      <div class="line">
        <svg width="9" height="9" viewBox="0 0 9 9"><circle cx="4.5" cy="4.5" r="4" fill="none" stroke="#fff"/><path d="M.5 4.5H8.5M4.5 .5C2.5 3 2.5 6 4.5 8.5M4.5 .5C6.5 3 6.5 6 4.5 8.5" fill="none" stroke="#fff" stroke-width=".7"/></svg>
        www.plimborex.au
      </div>
      <div class="line">
        <svg width="9" height="9" viewBox="0 0 9 9"><circle cx="4.5" cy="4.5" r="4" fill="none" stroke="#fff"/></svg>
        plimborex_au
      </div>
    </div>
  </div>

  <div class="page front-cover">
    <svg class="hex-ghost" style="left:150px;top:250px" width="220" height="230" viewBox="0 0 220 230"><polygon points="60,10 160,10 215,115 160,220 60,220 5,115" fill="none" stroke="#cadeef" stroke-width="18"/></svg>
    <svg class="cover-art" width="340" height="215" viewBox="0 0 340 215">
      <defs>
        <linearGradient id="bagTone" x1="0" y1="0" x2="1" y2="1"><stop offset="0" stop-color="#d9c7a3"/><stop offset=".5" stop-color="#eceae6"/><stop offset="1" stop-color="#c9a766"/></linearGradient>
        <linearGradient id="swoosh" x1="0" y1="1" x2="1" y2="0"><stop offset="0" stop-color="#0677ba"/><stop offset="1" stop-color="#7badd7"/></linearGradient>
      </defs>
      <path role="img" aria-label="Photo of stacked filter bags in tan, white and gold fabrics" d="M0 0H340V30C325 150 210 170 0 160Z" fill="url(#bagTone)"/>
      <path d="M340 30C325 150 210 170 0 160V185C200 195 335 160 340 95Z" fill="url(#swoosh)"/>
    </svg>
    <div class="brand" style="left:68px;top:232px">
      <div class="mark"></div>
      <div>
        <div class="name">PLIMBOREX</div>
        <div class="sub">ENVIRONMENTAL<br>SERVICES</div>
      </div>
    </div>
    <div class="abs cover-label" style="left:14px;top:344px">Plimborex Environmental Services</div>
    <h1 class="abs cover-title" style="left:14px;top:356px;width:300px">PREMIUM DUST COLLECTOR<br>SUPPLY &amp; EXPERT MAINTENANCE<br>SOLUTIONS</h1>
    <div class="abs cover-rule" style="left:0;top:410px;width:320px"></div>
    <p class="abs cover-blurb" style="left:14px;top:416px;width:270px">We provide accredited dust collection systems and comprehensive servicing to ensure industrial facilities maintain peak operational performance and environmental compliance.</p>
    <div class="abs url-tag" style="left:0;top:458px">WWW.PLIMBOREX.AU</div>
  </div>
</section>

<section class="spread inside">
  <div class="page services-page">
    <svg class="photo-oct" style="left:178px;top:0" width="162" height="240" viewBox="0 0 162 240">
      <polygon points="50,0 162,0 162,240 50,240 0,190 0,50" fill="#1b2d58"/>
      <polygon role="img" aria-label="Photo of a technician in protective suit installing filter bags" points="62,12 162,12 162,228 62,228 16,182 16,58" fill="#8f9aa6"/>
    </svg>
    <h2 class="abs h-section" style="left:16px;top:48px">OUR SERVICES</h2>
    <div class="abs h-sub" style="left:18px;top:70px;width:160px">INDUSTRIAL DUST COLLECTOR<br>SUPPLY &amp; EXPERT<br>MAINTENANCE RELIABILITY</div>
    <div class="abs body" style="left:18px;top:108px;width:152px">
      <p>Delivering advanced environmental solutions is at the core of what this business achieves for the industrial sector. We specialise in the supply and rigorous servicing of high-performance dust collectors designed to withstand the demanding conditions of Australia wide industrial sites. Our team focuses on ensuring your facility meets all necessary air quality standards through precise engineering and dedicated support.</p>
      <p>Maximising the lifespan of your equipment requires a partner who understands the intricacies of filtration technology. We offer a complete suite of services from initial supply to extraordinary maintenance, ensuring that every component functions at its absolute best. By choosing an accredited provider, you gain the assurance of technical excellence and a commitment to maintaining a clean, safe, and efficient workspace.</p>
    </div>
    <div class="services-panel">
      <h4>OUR SERVICES</h4>
      <ul>
        <li>Dust Collectors Servicing</li>
        <li>Dust Collectors Supply</li>
        <li>Dust Collectors Spare Parts Supply</li>
        <li>Filtration Bags Install</li>
        <li>Filtration Bags Supply</li>
        <li>Site Supervision &amp; Project Management</li>
        <li>Dust Collectors Regular Maintenance</li>
        <li>Dust Collectors Extraordinary Maintenance</li>
        <li>Dust Collector Inspection to Meet EPA Standards</li>
        <li>Leak Test</li>
        <li>Laboratory Analysis of Sample Bags</li>
      </ul>
    </div>
    <div class="svc" style="left:140px;top:312px">
      <h5>DUST COLLECTORS<br>SERVICING</h5>
      <p>We conduct thorough technical assessments and mechanical repairs to ensure your dust collection systems operate with maximum efficiency and reliability across all industrial applications.</p>
    </div>
    <div class="svc" style="left:246px;top:312px">
      <h5>DUST COLLECTORS<br>SUPPLY</h5>
      <p>Our team provides high-capacity, accredited dust collection units tailored to the specific volume and material requirements of your facility for optimal air filtration.</p>
    </div>
    <div class="svc" style="left:140px;top:398px">
      <h5>DUST COLLECTORS<br>SPARE PARTS SUPPLY</h5>
      <p>We stock and distribute essential components and high-quality spare parts to minimise downtime and keep your environmental systems running without interruption.</p>
    </div>
    <div class="svc" style="left:246px;top:398px">
      <h5>DUST COLLECTORS<br>SERVICING</h5>
      <p>We conduct thorough technical assessments and mechanical repairs to ensure your dust collection systems operate with maximum efficiency and reliability across all industrial applications.</p>
    </div>
  </div>

  <div class="page about-page">
    <svg class="photo-oct" style="left:162px;top:0" width="178" height="205" viewBox="0 0 178 205">
      <polygon points="50,0 178,0 178,205 50,205 0,155 0,50" fill="#1b2d58"/>
      <polygon role="img" aria-label="Photo of a filter bag housing interior with cage frames" points="62,12 178,12 178,193 62,193 16,147 16,58" fill="#9a9689"/>
    </svg>
    <h2 class="abs h-section" style="left:10px;top:48px">ABOUT US</h2>
    <div class="abs h-sub" style="left:12px;top:70px;width:148px">THE JOURNEY OF<br>ENVIRONMENTAL SERVICE<br>EXCELLENCE</div>
    <div class="abs body" style="left:12px;top:108px;width:144px">
      <p>Originating from a desire to provide more robust technical support to the Australia wide industrial sector, we began our journey by focusing on the critical need for reliable dust management. We recognised that many facilities struggled with maintaining complex filtration systems, and we stepped in to offer a more dedicated, hands-on approach. This foundation allowed us to build a reputation based on technical merit and unwavering support for our clients.</p>
    </div>
    <div class="abs body" style="left:12px;top:224px;width:300px">
      <p>Growing with the industries we serve, we have refined our processes to address the unique challenges of sectors like cement manufacturing, grain handling, lithium processing and power generation. We choose to aim for excellence because we understand that our work is vital to the operational continuity of our partners. Our history is one of continuous learning and adaptation, ensuring we remain at the forefront of environmental servicing and supply.</p>
    </div>
    <div class="why" role="img" aria-label="Navy-toned photo of an industrial plant behind the text">
      <div class="why-copy">
        <div class="k">WHY</div>
        <div class="big">CHOOSE <span>US?</span></div>
        <p>We bring over two decades of technical proficiency to every project, ensuring your systems are maintained by an accredited team.</p>
        <p>Our focus remains on delivering reliable outcomes that keep your operations compliant and efficient.</p>
      </div>
    </div>
    <div class="clients">
      <h4>OUR CLIENTS</h4>
      <div class="client-grid">
        <div class="client"><i></i>Norvale</div>
        <div class="client"><i></i>Stonegate</div>
        <div class="client"><i></i>Redfern Brick</div>
        <div class="client"><i></i>Kelbrook</div>
        <div class="client"><i></i>Tessaro</div>
        <div class="client"><i></i>Fibrelle</div>
        <div class="client"><i></i>Ashcombe</div>
        <div class="client"><i></i>Harbourline</div>
        <div class="client"><i></i>Goldfield</div>
        <div class="client"><i></i>Stonegate</div>
        <div class="client"><i></i>Southcem</div>
        <div class="client"><i></i>Westmere</div>
        <div class="client"><i></i>Civlane</div>
        <div class="client"><i></i>Orvitec</div>
      </div>
    </div>
  </div>
</section>

</body>
</html>
```